UK Supplement Company Needs a Label for Diet Protein Powder

We need a new, modern and fresh design for our Diet Protein Powder. Our protein powder is packaged in black plastic tubs (photo attached) and needs an attractive label. We would like to see designs that grab attention and look professional. We're very open to ideas. The label should be 88mm x 365mm. We also prefer PSD format where possible. These alterations could be made once your design is chosen. Have attached photo of our shake ingredients/benefits.

Target Market(s)

Slimmers

Industry/Entity Type

Health And Wellness

Font styles to use
Serif
Sans Serif

Colors

Designer to choose colors to be used in the design.

Requirements
Must have
• Clean, Modern and Professional Look. Eye catching. The flavour, we offer 6 flavours so this must be something we can edit (Flavours are Banana, Chocolate, Chocolate Mint, Strawberry, Toffee and Vanilla).
Nice to have
• Our logo, this can be VELTRA Nutrition or just VELTRA. Our logo files are attached.
Should not have
• We do not want to see people (faces or bodies) on the design.

```html
<!DOCTYPE html>
<html lang="en">
<head>
<meta charset="utf-8">
<title>VELTRA Diet Protein Powder – Labels</title>
<link rel="stylesheet" href="https://fonts.googleapis.com/css2?family=Open+Sans:wght@400;600;800&display=swap">
<style>
  :root {
    --page-bg: #ffffff;
    --strawberry-base: #951b20;
    --strawberry-disc: #c8282f;
    --strawberry-photo: #d8333a;
    --mint-base: #6a2f06;
    --mint-disc: #9a4b22;
    --mint-photo: #4a2a18;
    --text-light: #ffffff;
    --silver-light: #e6e6e6;
    --silver-mid: #9a9a9a;
    --silver-dark: #4c4c4c;
  }
  html, body {
    margin: 0;
    padding: 0;
    width: 1200px;
    height: 1200px;
    overflow: hidden;
    background: var(--page-bg);
  }
  .canvas {
    width: 1200px;
    height: 1200px;
    display: flex;
    align-items: center;
    justify-content: center;
    gap: 80px;
  }
  .label {
    width: 520px;
    height: 500px;
    display: block;
  }
  .label text {
    font-family: "Open Sans", sans-serif;
    fill: var(--text-light);
    text-anchor: middle;
  }
  .title-light { font-weight: 400; }
  .title-bold { font-weight: 800; }
  .brand-name { font-weight: 800; font-size: 30px; }
  .supplement-line { font-weight: 400; font-size: 21px; }
  .flavour-text { font-weight: 400; font-size: 11.5px; }
  .label--strawberry .label-base, .label--strawberry .brand-tab { fill: var(--strawberry-base); }
  .label--strawberry .label-disc { fill: var(--strawberry-disc); }
  .label--strawberry .flavour-photo { fill: var(--strawberry-photo); }
  .label--mint .label-base, .label--mint .brand-tab { fill: var(--mint-base); }
  .label--mint .label-disc { fill: var(--mint-disc); }
  .label--mint .flavour-photo { fill: var(--mint-photo); }
  .silver-stop-light { stop-color: var(--silver-light); }
  .silver-stop-mid { stop-color: var(--silver-mid); }
  .silver-stop-dark { stop-color: var(--silver-dark); }
</style>
</head>
<body>
<main class="canvas">

  <svg class="label label--strawberry" viewBox="0 0 520 500" role="group" aria-label="Strawberry flavour label">
    <defs>
      <linearGradient id="silver-ring-a" x1="0" y1="0" x2="1" y2="1">
        <stop offset="0" class="silver-stop-dark"/>
        <stop offset="0.35" class="silver-stop-light"/>
        <stop offset="0.65" class="silver-stop-mid"/>
        <stop offset="1" class="silver-stop-dark"/>
      </linearGradient>
      <linearGradient id="silver-band-a" x1="0" y1="0" x2="1" y2="0">
        <stop offset="0" class="silver-stop-dark"/>
        <stop offset="0.5" class="silver-stop-light"/>
        <stop offset="1" class="silver-stop-mid"/>
      </linearGradient>
    </defs>
    <rect class="label-base" x="0" y="0" width="520" height="500"/>
    <rect class="silver-band" x="0" y="6" width="520" height="10" fill="url(#silver-band-a)"/>
    <rect class="silver-band" x="0" y="482" width="520" height="18" fill="url(#silver-band-a)"/>
    <circle class="silver-ring" cx="260" cy="235" r="228" fill="url(#silver-ring-a)"/>
    <circle class="label-disc" cx="260" cy="235" r="206"/>
    <circle class="inner-ring" cx="260" cy="235" r="183" fill="none" stroke="#ffffff" stroke-width="1.5"/>
    <path class="brand-tab" d="M175 0 H350 V69 Q350 75 344 75 H181 Q175 75 175 69 Z"/>
    <text class="brand-name" x="262" y="52">VELTRA</text>
    <text class="title-light" x="260" y="160" font-size="66">DIET</text>
    <text class="title-bold" x="258" y="240" font-size="68">PROTEIN</text>
    <text class="title-light" x="258" y="313" font-size="68">POWDER</text>
    <text class="supplement-line" x="263" y="356">DIETARY</text>
    <text class="supplement-line" x="265" y="380">SUPPLEMENT</text>
    <ellipse class="flavour-photo" cx="400" cy="435" rx="30" ry="28" role="img" aria-label="Photo of fresh strawberries"/>
    <text class="flavour-text" x="470" y="440">STRAWBERRY</text>
    <text class="flavour-text" x="470" y="453">FLAVOUR</text>
  </svg>

  <svg class="label label--mint" viewBox="0 0 520 500" role="group" aria-label="Mint and chocolate flavour label">
    <defs>
      <linearGradient id="silver-ring-b" x1="0" y1="0" x2="1" y2="1">
        <stop offset="0" class="silver-stop-dark"/>
        <stop offset="0.35" class="silver-stop-light"/>
        <stop offset="0.65" class="silver-stop-mid"/>
        <stop offset="1" class="silver-stop-dark"/>
      </linearGradient>
      <linearGradient id="silver-band-b" x1="0" y1="0" x2="1" y2="0">
        <stop offset="0" class="silver-stop-dark"/>
        <stop offset="0.5" class="silver-stop-light"/>
        <stop offset="1" class="silver-stop-mid"/>
      </linearGradient>
    </defs>
    <rect class="label-base" x="0" y="0" width="520" height="500"/>
    <rect class="silver-band" x="0" y="6" width="520" height="10" fill="url(#silver-band-b)"/>
    <rect class="silver-band" x="0" y="482" width="520" height="18" fill="url(#silver-band-b)"/>
    <circle class="silver-ring" cx="260" cy="235" r="228" fill="url(#silver-ring-b)"/>
    <circle class="label-disc" cx="260" cy="235" r="206"/>
    <circle class="inner-ring" cx="260" cy="235" r="183" fill="none" stroke="#ffffff" stroke-width="1.5"/>
    <path class="brand-tab" d="M175 0 H350 V69 Q350 75 344 75 H181 Q175 75 175 69 Z"/>
    <text class="brand-name" x="262" y="52">VELTRA</text>
    <text class="title-light" x="260" y="160" font-size="66">DIET</text>
    <text class="title-bold" x="258" y="240" font-size="68">PROTEIN</text>
    <text class="title-light" x="258" y="313" font-size="68">POWDER</text>
    <text class="supplement-line" x="263" y="356">DIETARY</text>
    <text class="supplement-line" x="265" y="380">SUPPLEMENT</text>
    <ellipse class="flavour-photo" cx="390" cy="430" rx="46" ry="36" role="img" aria-label="Photo of mint leaves and chocolate curls"/>
    <text class="flavour-text" x="472" y="427">MINT &amp;</text>
    <text class="flavour-text" x="472" y="440">CHOCOLATE</text>
    <text class="flavour-text" x="472" y="453">FLAVOUR</text>
  </svg>

</main>
</body>
</html>
```